Pebble

My company name is pebble. The logo is attached. I am the business owner.
Name Gideon Thorpe
Phone number- 5553018826
email- Gideon_thorpe@quillnet.net
Website is not live yet but it will be workwithpebble.com
the current beta link is- https://site.brvhosting.com/pebble-v3/
on the back write “ find creative pros”
Use that beta link as reference for typography and colors on card.

```html
<!DOCTYPE html>
<html lang="en">
<head>
<meta charset="UTF-8">
<title>Pebble — Business Card</title>
<link href="https://fonts.googleapis.com/css2?family=Montserrat:wght@500;700;800&display=swap" rel="stylesheet">
<style>
  :root {
    --backdrop: #161616;
    --card: #262626;
    --logo-grey: #e4e4e4;
    --text-light: #ededed;
    --accent: #e27a17;
    --badge-text: #262626;
  }
  * { box-sizing: border-box; margin: 0; padding: 0; }
  html, body {
    width: 1200px;
    height: 900px;
    overflow: hidden;
    background: var(--backdrop);
    font-family: "Montserrat", Arial, sans-serif;
  }
  .canvas {
    position: relative;
    width: 1200px;
    height: 900px;
  }
  .card {
    position: absolute;
    left: 290px;
    width: 620px;
    height: 354px;
    background: var(--card);
    border-radius: 4px;
    box-shadow: 0 10px 30px rgba(0,0,0,0.45);
  }
  .card--front { top: 70px; }
  .card--back { top: 476px; }

  /* Front */
  .front-lockup {
    position: absolute;
    inset: 0;
    display: flex;
    flex-direction: column;
    align-items: center;
    justify-content: center;
  }
  .wordmark {
    color: var(--logo-grey);
    font-weight: 800;
    text-transform: uppercase;
    letter-spacing: -0.02em;
    line-height: 1;
  }
  .front-lockup .wordmark { font-size: 92px; }
  .tagline {
    margin-top: 14px;
    color: var(--accent);
    font-weight: 700;
    font-size: 17px;
    letter-spacing: 0.22em;
    text-transform: uppercase;
    align-self: center;
    padding-left: 120px;
  }

  /* Back */
  .back-logo {
    position: absolute;
    left: 60px;
    top: 200px;
    font-size: 56px;
  }
  .contact-block {
    position: absolute;
    left: 330px;
    top: 70px;
  }
  .holder-name {
    color: var(--text-light);
    font-weight: 800;
    font-size: 24px;
    text-transform: uppercase;
    letter-spacing: -0.01em;
  }
  .role-badge {
    display: inline-block;
    margin-top: 6px;
    background: var(--accent);
    color: var(--badge-text);
    font-weight: 700;
    font-size: 18px;
    padding: 1px 8px;
    text-transform: uppercase;
  }
  .contact-list {
    list-style: none;
    margin-top: 26px;
  }
  .contact-item {
    display: flex;
    align-items: center;
    gap: 10px;
    color: var(--text-light);
    font-weight: 500;
    font-size: 15px;
    line-height: 1.65;
  }
  .contact-icon {
    width: 16px;
    height: 16px;
    flex: none;
  }
</style>
</head>
<body>
<main class="canvas">

  <section class="card card--front" aria-label="Card front">
    <div class="front-lockup">
      <div class="wordmark">Pebble</div>
      <div class="tagline">Find creative pros</div>
    </div>
  </section>

  <section class="card card--back" aria-label="Card back">
    <div class="wordmark back-logo">Pebble</div>

    <div class="contact-block">
      <h1 class="holder-name">Gideon Thorpe</h1>
      <span class="role-badge">Owner</span>

      <ul class="contact-list">
        <li class="contact-item">
          <svg class="contact-icon" viewBox="0 0 16 16" fill="none" stroke="var(--accent)" stroke-width="1.4" stroke-linecap="round" stroke-linejoin="round">
            <path d="M3 2.5h2.5l1.2 3-1.6 1a8 8 0 0 0 4.4 4.4l1-1.6 3 1.2V13a1 1 0 0 1-1 1A11 11 0 0 1 2 3.5a1 1 0 0 1 1-1z"/>
          </svg>
          555-301-8826
        </li>
        <li class="contact-item">
          <svg class="contact-icon" viewBox="0 0 16 16" fill="none" stroke="var(--accent)" stroke-width="1.4" stroke-linejoin="round">
            <rect x="1.5" y="3.5" width="13" height="9"/>
            <path d="M1.5 3.5 8 9l6.5-5.5"/>
          </svg>
          Gideon_thorpe@quillnet.net
        </li>
        <li class="contact-item">
          <svg class="contact-icon" viewBox="0 0 16 16" fill="none" stroke="var(--accent)" stroke-width="1.4">
            <circle cx="8" cy="8" r="6.5"/>
            <ellipse cx="8" cy="8" rx="2.8" ry="6.5"/>
            <path d="M1.5 8h13"/>
          </svg>
          www.workwithpebble.com
        </li>
      </ul>
    </div>
  </section>

</main>
</body>
</html>
```